Business Card Design Project

Hollister Gray Fern Farms, LLC is a small farm south of Bandon Oregon. The farm produces blueberries, cranberries, mushrooms and possible other crops in the future.
We plan on installing yurts on the property for rent and for a farm experience,

A clody/misty covered black moon should be the design. This could be the entire front of the card. (There is another craft huddle project for this design). The back could be for the names, phone, address, etc.

Another option would be 3/4 of the card be the logo, then put the name, title, address, etc. vertically on the card right side front.

Target Market(s)

Customers of the farm, possible visitors using the yurts,

Industry/Entity Type

Farm

Other font styles liked:
• Hobo std

Colors

Designer to choose colors to be used in the design.

Requirements
Must have
• Consistent font usage

```html
<!DOCTYPE html>
<html lang="en">
<head>
<meta charset="utf-8">
<title>Gray Fern Farms – Business Card</title>
<link rel="stylesheet" href="https://fonts.googleapis.com/css2?family=Oswald:wght@500;600&display=swap">
<style>
  :root {
    --paper: #f5f4f1;
    --ink: #3a3c3d;
    --wash-light: #dfe5e5;
    --wash-mid: #c4cfd0;
    --card-edge: #3b3b3b;
    --lilac: #a97af8;
    --lilac-mist: #c3a6fb;
    --lilac-shadow: #9466e6;
    --white: #ffffff;
  }
  * { margin: 0; padding: 0; box-sizing: border-box; }
  html, body {
    width: 1144px;
    height: 1200px;
    overflow: hidden;
    background: var(--paper);
    font-family: "Oswald", "Arial Narrow", sans-serif;
  }
  .canvas {
    position: relative;
    width: 1144px;
    height: 1200px;
  }

  /* Front face */
  .card-front {
    position: absolute;
    left: 0; top: 0;
    width: 1144px;
    height: 602px;
    background: var(--paper);
    border: 2px solid var(--card-edge);
    border-bottom-width: 3px;
  }
  .brand-name {
    position: absolute;
    left: 0; right: 0;
    top: 140px;
    text-align: center;
    font-weight: 500;
    font-size: 44px;
    letter-spacing: 4px;
    color: var(--ink);
    text-transform: uppercase;
  }
  .mist-artwork {
    position: absolute;
    left: 421px;
    top: 213px;
    width: 342px;
    height: 190px;
    background: radial-gradient(ellipse at 50% 50%, var(--wash-mid) 0%, var(--wash-light) 70%, rgba(223,229,229,0) 100%);
  }
  .brand-place {
    position: absolute;
    left: 0; right: 0;
    top: 405px;
    text-align: center;
    font-weight: 500;
    font-size: 36px;
    color: var(--ink);
  }

  /* Back face */
  .card-back {
    position: absolute;
    left: 0; top: 602px;
    width: 1144px;
    height: 598px;
    background: var(--lilac);
    overflow: hidden;
  }
  .cloud-artwork {
    position: absolute;
    left: 0; top: 180px;
    width: 1144px;
    height: 418px;
    background:
      radial-gradient(ellipse 260px 70px at 320px 110px, rgba(195,166,251,0.8), rgba(195,166,251,0) 100%),
      radial-gradient(ellipse 200px 60px at 180px 300px, rgba(195,166,251,0.7), rgba(195,166,251,0) 100%),
      radial-gradient(ellipse 420px 140px at 850px 320px, rgba(195,166,251,0.85), rgba(195,166,251,0) 100%),
      radial-gradient(ellipse 240px 90px at 1060px 100px, rgba(195,166,251,0.7), rgba(195,166,251,0) 100%),
      linear-gradient(180deg, rgba(148,102,230,0) 0%, rgba(148,102,230,0.25) 100%);
  }
  .holder {
    position: absolute;
    right: 577px;
    top: 248px;
    text-align: right;
    color: var(--white);
  }
  .holder-name {
    font-weight: 600;
    font-size: 55px;
    line-height: 1;
    letter-spacing: 0.5px;
  }
  .holder-title {
    margin-top: 6px;
    font-weight: 600;
    font-size: 19px;
  }
  .contact-list {
    position: absolute;
    left: 644px;
    top: 183px;
    list-style: none;
    color: var(--white);
  }
  .contact-item {
    position: absolute;
    left: 0;
    display: flex;
    align-items: center;
    white-space: nowrap;
    font-weight: 600;
    font-size: 17px;
  }
  .contact-item svg { width: 36px; height: 36px; margin-right: 15px; flex: none; }
  .contact-web { top: 0; }
  .contact-mail { top: 63px; }
  .contact-phone { top: 119px; }
  .contact-address { top: 186px; }
</style>
</head>
<body>
<main class="canvas">

  <section class="card-front" aria-label="Card front">
    <div class="brand-name">Gray Fern Farms</div>
    <div class="mist-artwork" role="img" aria-label="Soft grey watercolour wash with drifting mist"></div>
    <div class="brand-place">Hollister, Oregon</div>
  </section>

  <section class="card-back" aria-label="Card back">
    <div class="cloud-artwork" role="img" aria-label="Soft lilac clouds drifting across the lower card"></div>

    <div class="holder">
      <div class="holder-name">Ray T. Hollis</div>
      <div class="holder-title">Tittle Gray Fern Farm</div>
    </div>

    <ul class="contact-list">
      <li class="contact-item contact-web">
        <svg viewBox="0 0 36 36" aria-hidden="true">
          <rect x="3" y="6" width="30" height="20" fill="none" stroke="#fff" stroke-width="2"/>
          <line x1="12" y1="31" x2="24" y2="31" stroke="#fff" stroke-width="2"/>
        </svg>
        www.grayfernfarm.com
      </li>
      <li class="contact-item contact-mail">
        <svg viewBox="0 0 36 36" aria-hidden="true">
          <rect x="3" y="8" width="30" height="21" fill="#fff"/>
          <path d="M3 8 L18 20 L33 8" fill="none" stroke="var(--lilac)" stroke-width="2"/>
        </svg>
        grayfern@farmmail.com
      </li>
      <li class="contact-item contact-phone">
        <svg viewBox="0 0 36 36" aria-hidden="true">
          <path d="M10 4 L15 4 L16 11 L12.5 13 C14 18 17 22 22 24 L24 20.5 L31 22 L31 27 C31 29 29 31 27 31 C16 30 6 20 5 9 C5 6 7 4 10 4 Z" fill="#fff"/>
        </svg>
        425.555.0148
      </li>
      <li class="contact-item contact-address">
        <svg viewBox="0 0 36 36" aria-hidden="true">
          <path d="M18 34 L9 18 A10 10 0 1 1 27 18 Z" fill="#fff"/>
          <circle cx="18" cy="12" r="5" fill="var(--lilac)"/>
        </svg>
        Gray Fern Street No. 3
      </li>
    </ul>
  </section>

</main>
</body>
</html>
```